Yard Sign Design Needed

Yard sign needed for mowing & landscaping company. Would like to use the top logo with black background which is attached. Would like MOWING to be in large standout letters. The word "landscaping" can be smaller and more artistic or omitted. Will need room for phone number once design is approved. The phone number will need to stand out and look identical/similar to the word 'MOWING"

```html
<!DOCTYPE html>
<html lang="en">
<head>
<meta charset="utf-8">
<title>Norvale Contractors – Mowing Yard Sign</title>
<link rel="stylesheet" href="https://fonts.googleapis.com/css2?family=Exo+2:wght@400;700;800&family=Ubuntu:wght@700&display=swap">
<style>
  :root {
    --sign-green: #8fa83e;
    --sign-black: #070808;
    --sign-white: #ffffff;
  }
  html, body {
    margin: 0;
    padding: 0;
    width: 1200px;
    height: 1004px;
    overflow: hidden;
    background: var(--sign-black);
  }
  .yard-sign {
    display: block;
    width: 1200px;
    height: 1004px;
  }
  .phone-band, .divider-green, .name-mark { fill: var(--sign-green); }
  .panel-black { fill: var(--sign-black); }
  .web-strip { fill: var(--sign-white); }
  .phone-number {
    font-family: "Ubuntu", sans-serif;
    font-weight: 700;
    font-size: 176px;
    fill: var(--sign-white);
  }
  .service-main {
    font-family: "Exo 2", sans-serif;
    font-weight: 700;
    font-size: 232px;
    fill: var(--sign-white);
  }
  .service-sub {
    font-family: "Exo 2", sans-serif;
    font-weight: 400;
    font-size: 74px;
    fill: var(--sign-white);
  }
  .website {
    font-family: "Ubuntu", sans-serif;
    font-weight: 700;
    font-size: 49px;
    fill: var(--sign-green);
  }
  .company-name {
    font-family: "Ubuntu", sans-serif;
    font-weight: 700;
    font-size: 30px;
    fill: var(--sign-green);
  }
</style>
</head>
<body>
<svg class="yard-sign" viewBox="0 0 1200 1004" xmlns="http://www.w3.org/2000/svg" role="img" aria-label="Norvale Contractors mowing and landscaping yard sign">
  <rect class="phone-band" x="0" y="0" width="1200" height="246"/>
  <rect class="panel-black" x="0" y="246" width="1200" height="758"/>
  <rect class="divider-green" x="0" y="256" width="1200" height="5"/>
  <text class="phone-number" x="106" y="206" textLength="993" lengthAdjust="spacingAndGlyphs">+12 345 6789</text>

  <text class="service-main" x="84" y="561" textLength="1031" lengthAdjust="spacingAndGlyphs">MOWING</text>
  <text class="service-sub" x="74" y="673" textLength="644" lengthAdjust="spacingAndGlyphs">LANDSCAPING</text>

  <rect class="divider-green" x="0" y="855" width="757" height="5"/>
  <polygon class="web-strip" points="0,869 751,869 712,1004 0,1004"/>
  <text class="website" x="71" y="937" textLength="565" lengthAdjust="spacingAndGlyphs">NORVALECONTRACTORS.COM</text>

  <rect class="name-mark" x="794" y="876" width="20" height="20"/>
  <text class="company-name" x="826" y="897" textLength="322" lengthAdjust="spacingAndGlyphs">NORVALE CONTRACTORS LLC</text>
</svg>
</body>
</html>
```